Powerpoint Slides for 'Lantern Ridge | consulting' firm

Hello,

I would like a suite of slides to not be typical of just ANOther deck. My business name is 'Lantern Ridge | consulting', so I would like to see innovation and creativity translated into the slides.

1. ‘Company/Cover Page’ – should showcase Lantern Ridge | consulting branding; perhaps with some animation to give the sense of 'out of the box' content.
The company name, Lantern Ridge | consulting, and tagline - Strategise | Organise | Optimise | Communicate, should appear together on the front and end page. The company name should appear on all other pages
2. Master branded background slide, with suggested font, and ideally with some colour options which could be leveraged in longer presentations to ‘break’ it up
3. Master branded background slide with an option to include bulleted content within some type of e.g. shape/form (not just as bullets against a blank background)
4. Divider slide (possibly leveraging some of the colours in Point 2

I have attached a copy of the logo/layout of my business card. The square used is raised on the business card which gives a very subtle effect of literally being out of the box. I would like something of a similar feel, but with colour (as noted in Point 2), though very open to ideas/suggestions.

Many Thanks,
Marisol
Updates

This project has been re-opened to all designers. I look forward to seeing creative and innovative submissions. Best Regards, Marisol

Target Market(s)

SMEs and Corporates - however, I don't want to look like just any other consultancy company.

Industry/Entity Type

Business

Colors

Designer to choose colors to be used in the design.

Requirements
Must have
• Innovation; Creativity; Professionalism; Succinct

```html
<!DOCTYPE html>
<html lang="en">
<head>
<meta charset="utf-8">
<title>Lantern Ridge | consulting – slide suite</title>
<link rel="stylesheet" href="https://fonts.googleapis.com/css2?family=Carlito:wght@400;700&display=swap">
<style>
  :root {
    --canvas: #ffffff;
    --amber: #ffc000;
    --lime: #a9d04b;
    --paper: #ffffff;
    --ink: #000000;
    --ink-soft: #3a3a3a;
    --tangerine: #ed7d31;
    --tangerine-edge: #c55a11;
    --parchment-light: #fdf3df;
    --parchment-dark: #f6e4c2;
    --outline: #5b8fb0;
    --font-main: "Carlito", "Calibri", Arial, sans-serif;
  }
  * { box-sizing: border-box; margin: 0; padding: 0; }
  html, body {
    width: 1200px; height: 900px; overflow: hidden;
    background: var(--canvas);
    font-family: var(--font-main);
    color: var(--ink);
  }
  h1, h2, p, li { font-weight: 400; }
  .slide-grid { position: relative; width: 1200px; height: 900px; }
  .slide { position: absolute; overflow: hidden; background: var(--amber); }

  .slide--cover {
    left: 5px; top: 5px; width: 593px; height: 442px;
    background: linear-gradient(to bottom, var(--lime) 0, var(--amber) 50px, var(--amber) 390px, var(--lime) 100%);
  }
  .slide--master {
    left: 603px; top: 5px; width: 592px; height: 442px;
    background: linear-gradient(to bottom, var(--lime) 0, var(--amber) 55px, var(--amber) 100%);
  }
  .slide--bullets {
    left: 5px; top: 452px; width: 593px; height: 443px;
    background: linear-gradient(to bottom, var(--amber) 0, var(--amber) 390px, var(--lime) 100%);
  }
  .slide--divider {
    left: 603px; top: 452px; width: 592px; height: 443px;
    background: linear-gradient(to bottom, var(--lime) 0, var(--amber) 55px, var(--amber) 100%);
  }

  .slide-art { position: absolute; inset: 0; width: 100%; height: 100%; }
  .cover-title { font-size: 49px; fill: var(--ink); }
  .divider-title { font-size: 45px; fill: var(--ink); }

  .master-title {
    position: absolute; left: 45px; top: 20px;
    font-size: 33px; line-height: 1; letter-spacing: 0.3px;
  }
  .master-body {
    position: absolute; left: 45px; top: 103px;
    font-size: 20px; line-height: 1; letter-spacing: 0.4px;
  }

  .bullet-title-box {
    position: absolute; left: 37px; top: 31px; width: 515px; height: 62px;
    background: var(--paper); border: 1px solid #7f7f7f;
    font-size: 29px; line-height: 60px; padding-left: 7px; letter-spacing: 0.3px;
  }
  .content-post {
    position: absolute; left: 283px; width: 31px;
    background: var(--tangerine); border: 1px solid var(--tangerine-edge);
  }
  .content-post--top { top: 107px; height: 10px; }
  .content-post--bottom { top: 405px; height: 33px; }
  .content-board {
    position: absolute; left: 39px; top: 116px; width: 515px; height: 290px;
    background: radial-gradient(ellipse at 40% 40%, var(--parchment-light), var(--parchment-dark));
    border: 1px solid #bfae8e;
  }
  .content-board-list {
    position: absolute; left: 40px; top: 120px;
    list-style: none; font-size: 19px; line-height: 1.2; letter-spacing: 0.5px;
  }
  .content-board-list li::before { content: "•"; margin: 0 6px 0 3px; }

  .brand-mark {
    position: absolute; font-size: 13px; line-height: 1.2; color: var(--ink-soft);
    letter-spacing: 0.3px;
  }
  .brand-mark--cover { left: 16px; bottom: 8px; }
  .brand-tagline { display: block; font-size: 11px; }
  .brand-mark--corner { right: 16px; bottom: 10px; }
</style>
</head>
<body>
<main class="slide-grid">

  <section class="slide slide--cover" aria-label="Company cover page">
    <svg class="slide-art" viewBox="0 0 593 442">
      <polygon points="10,198 435,93 416,7 592,147 498,352 480,267 51,370"
               fill="var(--paper)" stroke="var(--outline)" stroke-width="1"/>
      <text class="cover-title" x="270" y="252" text-anchor="middle"
            transform="rotate(-15 270 238)">Company/Cover Page</text>
    </svg>
    <p class="brand-mark brand-mark--cover">Lantern Ridge | consulting
      <span class="brand-tagline">Strategise | Organise | Optimise | Communicate</span></p>
  </section>

  <section class="slide slide--master" aria-label="Master branded background slide">
    <h2 class="master-title">Master branded background slide</h2>
    <p class="master-body">Master branded background slide</p>
    <p class="brand-mark brand-mark--corner">Lantern Ridge | consulting</p>
  </section>

  <section class="slide slide--bullets" aria-label="Master branded background slide 2">
    <svg class="slide-art" viewBox="0 0 593 443">
      <polyline points="37,31 295,0 552,31" fill="none" stroke="#404040" stroke-width="1"/>
    </svg>
    <div class="content-post content-post--top"></div>
    <div class="content-post content-post--bottom"></div>
    <h2 class="bullet-title-box">Master branded background slide 2</h2>
    <div class="content-board" role="img" aria-label="Parchment-textured content panel"></div>
    <ul class="content-board-list">
      <li>Master branded background slide 2</li>
    </ul>
    <p class="brand-mark brand-mark--corner">Lantern Ridge | consulting</p>
  </section>

  <section class="slide slide--divider" aria-label="Divider slide">
    <svg class="slide-art" viewBox="0 0 592 443">
      <polygon points="62,97 576,174 550,358 33,282"
               fill="var(--paper)" stroke="var(--outline)" stroke-width="1"/>
      <text class="divider-title" x="52" y="210" transform="rotate(8.5 52 210)">Divider slide</text>
    </svg>
    <p class="brand-mark brand-mark--corner">Lantern Ridge | consulting</p>
  </section>

</main>
</body>
</html>
```